Dolsemk Business Cards

Business cards for real estate
Target Market(s)
Real estate
Industry/Entity Type
Real Estate Agent
Font styles to use
Serif
Requirements
Must have
- Photo and logo

```html
<!DOCTYPE html>
<html lang="en">
<head>
<meta charset="utf-8">
<title>Dolsemk Realty Business Cards</title>
<link href="https://fonts.googleapis.com/css2?family=Cinzel:wght@400;500&family=Lato:wght@400&display=swap" rel="stylesheet">
<style>
  :root {
    --page: #1b1b1d;
    --card: #121213;
    --white: #f2f2f2;
    --grey: #c9c9c9;
    --gold: #d2a64a;
    --crimson: #9c1f2c;
    --photo-dark: #0d0d0f;
    --photo-mid: #2a2d36;
    --photo-light: #5a6070;
  }
  * { margin: 0; padding: 0; box-sizing: border-box; }
  html, body { width: 1200px; height: 900px; overflow: hidden; background: var(--page); }
  .canvas { position: relative; width: 1200px; height: 900px; }
  .card {
    position: absolute; left: 320px; width: 560px; height: 320px;
    background: var(--card); border-radius: 22px; overflow: hidden;
    box-shadow: 0 14px 34px rgba(0,0,0,.55);
  }
  .card--front { top: 70px; }
  .card--back { top: 500px; }

  .brand {
    position: absolute; left: 50%; top: 50%; transform: translate(-50%, -50%);
    display: flex; align-items: center; gap: 18px;
  }
  .brand__dot { width: 54px; height: 54px; border-radius: 50%; background: var(--crimson); }
  .brand__name {
    font-family: "Cinzel", Georgia, serif; font-weight: 400; color: var(--white);
    font-size: 34px; line-height: 1; letter-spacing: 1px;
  }
  .brand__name span { display: block; font-size: 22px; letter-spacing: 7px; margin-top: 4px; }

  .agent { position: absolute; left: 36px; bottom: 30px; }
  .agent__name {
    font-family: "Cinzel", Georgia, serif; font-weight: 400; color: var(--gold);
    font-size: 22px; letter-spacing: 1px; line-height: 1.1;
  }
  .agent__role {
    font-family: "Lato", Arial, sans-serif; color: var(--grey);
    font-size: 15px; margin-bottom: 10px;
  }
  .contact { list-style: none; font-family: "Lato", Arial, sans-serif; color: var(--grey); font-size: 15px; line-height: 1.45; }
  .contact li { display: flex; align-items: center; gap: 8px; }
  .contact svg { width: 13px; height: 13px; flex: none; }
  .contact__address { margin-top: 6px; display: block !important; }

  .portrait {
    position: absolute; right: 0; top: 30px; width: 260px; height: 290px;
    background: radial-gradient(ellipse at 50% 35%, var(--photo-light) 0%, var(--photo-mid) 40%, var(--photo-dark) 80%);
  }
</style>
</head>
<body>
<main class="canvas">
  <section class="card card--front">
    <div class="brand">
      <div class="brand__dot"></div>
      <div class="brand__name">DOLSEMK<span>REALTY</span></div>
    </div>
  </section>

  <section class="card card--back">
    <div class="portrait" role="img" aria-label="Portrait photo of the managing director in a dark suit and blue tie"></div>
    <div class="agent">
      <h1 class="agent__name">MARCUS HALE</h1>
      <p class="agent__role">Managing Director</p>
      <ul class="contact">
        <li>
          <svg viewBox="0 0 16 16"><path fill="#d2a64a" d="M3 1l3 3-2 2c1 2 3 4 5 5l2-2 3 3-2 3C6 15 1 10 1 3z"/></svg>
          044-987 654 321
        </li>
        <li>
          <svg viewBox="0 0 16 16"><rect x="1" y="3" width="14" height="10" fill="#d2a64a"/><path d="M1 3l7 6 7-6" stroke="#121213" stroke-width="1.4" fill="none"/></svg>
          hello@dolsemk.com
        </li>
        <li>
          <svg viewBox="0 0 16 16"><circle cx="8" cy="8" r="7" fill="#d2a64a"/><path d="M1 8h14M8 1c-3 4-3 10 0 14M8 1c3 4 3 10 0 14" stroke="#121213" stroke-width="1" fill="none"/></svg>
          www.dolsemkrealty.com
        </li>
        <li class="contact__address">87 Harbor Lane, Suite 5,<br>60218, Marlow Bay</li>
      </ul>
    </div>
  </section>
</main>
</body>
</html>
```